Landing page для Vamlor parts
Название сайта (домена, или проекта)
Vamlor parts
Выберите сайты-победители прошлых конкурсов, чтобы дизайнерам был понятен нужный вам стиль
Укажите ссылки на сайты, которые нравятся
https://tridovka.ru/
Оптово-розничные покупатели оригинальных запчастей на автомобили. Средний чек от 30 000 рублей. Мужчины. Мы возим только оригинальные запчасти из Европы, у нас высокая скорость доставки! от 5 рабочих дней.
Этот сайт в принципе нравится https://palmesto.ru/?ysclid=qwert7xz2b814263590 ( не сама цветовая гамма) а расположение блоков.
У нас сайт создан на платформе KRUM. Платформа предполагает использование шаблонных вариантов сайта, то есть сайт реализован на готовом шаблоне. Ниже мы прикладываем используемый шаблон.
https://vamlor-parts.ru/?templateId=31&class=301&color=206351
Важно учитывать, что выход за рамки возможностей шаблона невозможен. Поэтому макет дизайна лендинг-пейджа по техническому заданию, представленному ниже, необходимо разрабатывать строго с учётом функциональных и визуальных возможностей, которые предоставляет данный шаблон сайта.
https://docs.example-files.net/document/d/7Kd_prTq2mXz9WbLe4HnRs0VyUj3cAoF8QgtZ1NxYbPw/edit?tab=t.0
Адаптивность сайта
Десктопная версия, Версия для планшетов, Версия для телефонов

```html
<!DOCTYPE html>
<html lang="ru">
<head>
<meta charset="utf-8">
<title>Vamlor parts — лендинг</title>
<link href="https://fonts.googleapis.com/css2?family=Unbounded:wght@300;400&family=Manrope:wght@400;500;600&display=swap" rel="stylesheet">
<style>
:root{
  --stage:#2c3142;
  --screen:#0b0b0e;
  --card:#1b1c21;
  --card-line:#2c2e36;
  --field:#25262d;
  --text:#f3f3f5;
  --muted:#8d8f99;
  --faint:#5d5f69;
  --accent-red:#b8433a;
  --accent-blue:#33405e;
}
*{box-sizing:border-box;margin:0;padding:0}
html,body{width:1200px;height:915px;overflow:hidden}
body{background:var(--stage);font-family:"Manrope",sans-serif;color:var(--text);position:relative}
.display{font-family:"Unbounded",sans-serif;font-weight:300}

/* tablet view */
.tablet{position:absolute;left:30px;top:40px;width:760px;height:875px;background:var(--screen);border-radius:26px 26px 0 0;overflow:hidden}
.stats-label{position:absolute;left:28px;top:70px;font-size:15px;line-height:1.3;font-weight:500}
.stat{position:absolute;background:var(--card);border-radius:12px;padding:18px 16px}
.stat__value{font-size:38px;line-height:1.1;white-space:nowrap}
.stat__value--sm{font-size:34px}
.stat__caption{font-size:15px;color:var(--muted);margin-top:4px;white-space:nowrap}
.process{position:absolute;left:0;top:323px;width:760px;height:342px;
  background:radial-gradient(ellipse at 78% 25%,#d9b9c0 0%,#9c4f63 10%,transparent 30%),
  radial-gradient(ellipse at 20% 40%,var(--accent-red) 0%,transparent 45%),
  radial-gradient(ellipse at 55% 65%,#b05a3e 0%,transparent 35%),
  linear-gradient(135deg,#4a3d5c 0%,var(--accent-blue) 45%,#1a1e2c 100%)}
.process__content{position:absolute;left:0;top:323px;width:760px;height:342px}
.process__title{position:absolute;left:28px;top:96px;font-size:26px;line-height:1.2;white-space:nowrap}
.steps{position:absolute;left:18px;top:146px;display:flex;gap:7px}
.step{flex:0 0 180px;height:196px;background:rgba(30,30,40,.45);border:1px solid rgba(255,255,255,.12);border-radius:10px 10px 0 0;padding:14px 12px;font-size:17px;font-weight:500;line-height:1.25;position:relative}
.step svg{position:absolute;left:60px;bottom:44px}
.panel{position:absolute;top:677px;height:175px;background:var(--card);border-radius:12px;padding:18px 14px}
.panel__title{font-size:18px;font-weight:500;margin-bottom:14px}
.field{height:24px;background:var(--field);border-radius:5px;font-size:9px;color:var(--faint);display:flex;align-items:center;justify-content:space-between;padding:0 8px}
.note{font-size:9.5px;color:var(--muted);line-height:1.4;margin:12px 0 10px}
.btn{display:inline-flex;align-items:center;justify-content:center;border:1px solid #c9cad0;border-radius:5px;font-size:10px;padding:0 12px;height:27px;color:var(--text)}
.btn--off{border-color:var(--card-line);color:var(--faint)}
.grid2{display:grid;grid-template-columns:1fr 1fr;gap:8px 10px;margin-bottom:14px}
.chev{width:7px;height:7px}

/* phones */
.phone{position:absolute;background:var(--screen);border-radius:30px;overflow:hidden}
.phone--hero{left:694px;top:111px;width:257px;height:557px;z-index:2;box-shadow:0 0 0 1px #3a3d48}
.phone--form{left:917px;top:214px;width:274px;height:566px;z-index:1}
.header{position:absolute;left:0;top:28px;width:100%;display:flex;align-items:center;padding:0 10px;gap:8px;font-size:10px}
.brand{font-weight:600;font-size:11px;letter-spacing:.04em;margin-right:auto}
.icon-box{width:22px;height:22px;background:var(--card);border-radius:5px;display:flex;align-items:center;justify-content:center}
.hero{position:absolute;left:0;top:62px;width:100%;height:410px;
  background:radial-gradient(ellipse at 80% 55%,#9a4a55 0%,transparent 35%),
  radial-gradient(ellipse at 20% 65%,#55607a 0%,transparent 45%),
  linear-gradient(180deg,#1d2230 0%,#2e3447 50%,#0d0e13 100%)}
.hero__content{position:absolute;left:0;top:62px;width:100%;height:410px}
.hero__title{position:absolute;left:16px;top:28px;width:215px;font-size:21px;line-height:1.28}
.hero__sub{position:absolute;left:16px;top:166px;font-size:10px}
.hero__cta{position:absolute;left:16px;top:296px;width:225px;height:30px;font-size:11px}
.hero__link{position:absolute;left:0;top:346px;width:100%;text-align:center;font-size:10px;text-decoration:underline}
.m-card{position:absolute;background:var(--card);border-radius:12px;padding:16px 14px}
.m-card__title{font-size:15px;font-weight:500;line-height:1.25}
.m-field{height:28px;background:var(--field);border-radius:5px;font-size:9px;color:var(--faint);display:flex;align-items:center;justify-content:space-between;padding:0 9px;margin-bottom:8px}
</style>
</head>
<body>

<section class="tablet">
  <p class="stats-label">Наша работа<br>в цифрах</p>
  <div class="stat" style="left:159px;top:58px;width:291px;height:152px"><p class="stat__value display">10 лет</p><p class="stat__caption">на рынке</p></div>
  <div class="stat" style="left:455px;top:58px;width:290px;height:152px"><p class="stat__value display">27 000 +</p><p class="stat__caption">довольных клиентов</p></div>
  <div class="stat" style="left:159px;top:216px;width:291px;height:100px"><p class="stat__value stat__value--sm display">2 офиса:</p><p class="stat__caption">Москва и Санкт-Петербург</p></div>
  <div class="stat" style="left:455px;top:216px;width:290px;height:100px"><p class="stat__value stat__value--sm display">80 %</p><p class="stat__caption">повторных обращений</p></div>

  <div class="process" role="img" aria-label="Фото фары автомобиля в красно-синих тонах"></div>
  <div class="process__content">
    <h2 class="process__title display">Как мы работаем</h2>
    <div class="steps">
      <div class="step">Вы оставляете заявку / VIN<svg width="60" height="30" viewBox="0 0 60 30"><path d="M0 15H58M44 1L58 15L44 29" fill="none" stroke="#fff" stroke-width="1"/></svg></div>
      <div class="step">Мы подбираем оригинальную деталь<svg width="60" height="30" viewBox="0 0 60 30"><path d="M0 15H58M44 1L58 15L44 29" fill="none" stroke="#fff" stroke-width="1"/></svg></div>
      <div class="step">Согласуем сроки и стоимость<svg width="60" height="30" viewBox="0 0 60 30"><path d="M0 15H58M44 1L58 15L44 29" fill="none" stroke="#fff" stroke-width="1"/></svg></div>
      <div class="step">Доставка и гарантия</div>
    </div>
  </div>

  <div class="panel" style="left:13px;width:395px">
    <h3 class="panel__title">Онлайн-помощь специалиста</h3>
    <div class="field"><span>VIN или вопрос по автомобилю</span><span>ⓘ Как заполнить</span></div>
    <p class="note">Более 10 специалистов прямо сейчас готовы вас проконсультировать.<br>Примерное время ожидания ответа на Ваш запрос 3-10 минут.</p>
    <span class="btn">Отправить запрос специалисту</span>
  </div>
  <div class="panel" style="left:413px;width:335px">
    <h3 class="panel__title">Подбор по автомобилю</h3>
    <div class="grid2">
      <div class="field"><span>Год выпуска</span><svg class="chev" viewBox="0 0 8 8"><path d="M1 2l3 3 3-3" fill="none" stroke="#5d5f69"/></svg></div>
      <div class="field"><span>Марка</span><svg class="chev" viewBox="0 0 8 8"><path d="M1 2l3 3 3-3" fill="none" stroke="#5d5f69"/></svg></div>
      <div class="field"><span>Модель</span><svg class="chev" viewBox="0 0 8 8"><path d="M1 2l3 3 3-3" fill="none" stroke="#5d5f69"/></svg></div>
      <div class="field"><span>Модификация</span><svg class="chev" viewBox="0 0 8 8"><path d="M1 2l3 3 3-3" fill="none" stroke="#5d5f69"/></svg></div>
    </div>
    <span class="btn btn--off" style="width:160px">Перейти</span>
  </div>
</section>

<section class="phone phone--hero">
  <header class="header">
    <span class="brand">VAMLOR</span>
    <span>☰ Каталог</span>
    <span class="icon-box"><svg width="11" height="11" viewBox="0 0 12 12"><circle cx="5" cy="5" r="3.8" fill="none" stroke="#fff"/><path d="M8 8l3 3" stroke="#fff"/></svg></span>
    <span class="icon-box"><svg width="12" height="11" viewBox="0 0 12 11"><path d="M0.5 1h2l1.5 6h6l1.5-4.5H3" fill="none" stroke="#fff"/><circle cx="4.5" cy="9.5" r="1" fill="#fff"/><circle cx="9" cy="9.5" r="1" fill="#fff"/></svg></span>
    <span class="icon-box"><svg width="12" height="12" viewBox="0 0 12 12"><circle cx="6" cy="6" r="5.3" fill="none" stroke="#fff"/><circle cx="6" cy="4.8" r="1.8" fill="none" stroke="#fff"/></svg></span>
  </header>
  <div class="hero" role="img" aria-label="Фото автомобиля в тёмных тонах"></div>
  <div class="hero__content">
    <h1 class="hero__title display">Оригинальные автозапчасти из&nbsp;Европы</h1>
    <p class="hero__sub">С доставкой от 3 рабочих дней</p>
    <span class="btn hero__cta">Подобрать запчасть</span>
    <p class="hero__link">Получить консультацию</p>
  </div>
  <div class="m-card" style="left:8px;top:482px;width:241px;height:90px">
    <h3 class="m-card__title">Онлайн-помощь<br>специалиста</h3>
  </div>
</section>

<section class="phone phone--form">
  <div class="m-card" style="left:8px;top:-10px;width:258px;height:200px;padding-top:30px">
    <h3 class="m-card__title" style="margin-bottom:14px">Онлайн-помощь<br>специалиста</h3>
    <div class="m-field"><span>Ваш вопрос по автомобилю</span><span>ⓘ</span></div>
    <p class="note" style="margin:8px 0">Более 10 специалистов прямо сейчас готовы вас проконсультировать. Примерное время ожидания ответа на Ваш запрос 3-10 минут.</p>
    <span class="btn" style="width:100%;height:28px">Отправить запрос специалисту</span>
  </div>
  <div class="m-card" style="left:8px;top:198px;width:258px;height:262px">
    <h3 class="m-card__title" style="margin-bottom:14px">Подбор по автомобилю</h3>
    <div class="m-field"><span>Год выпуска</span><svg class="chev" viewBox="0 0 8 8"><path d="M1 2l3 3 3-3" fill="none" stroke="#5d5f69"/></svg></div>
    <div class="m-field"><span>Марка</span><svg class="chev" viewBox="0 0 8 8"><path d="M1 2l3 3 3-3" fill="none" stroke="#5d5f69"/></svg></div>
    <div class="m-field"><span>Модель</span><svg class="chev" viewBox="0 0 8 8"><path d="M1 2l3 3 3-3" fill="none" stroke="#5d5f69"/></svg></div>
    <div class="m-field"><span>Модификация</span><svg class="chev" viewBox="0 0 8 8"><path d="M1 2l3 3 3-3" fill="none" stroke="#5d5f69"/></svg></div>
    <span class="btn btn--off" style="width:100%;height:30px;margin-top:6px">Перейти</span>
  </div>
</section>

</body>
</html>
```